Business Card Design for Concierge business

Hi. I would like to have an elegant, smart business card for my concierge business, called Harbor Concierge. The services I provide are mail management, dog walking, cleaning, car, stylist, personal shopper, running errands, property management, event planning. I was thinking to add my picture but I would like to see options without it as well, if possible.

Thank you.

Business Card Details:
*Designers are to solely use contact information for the business card design. This is not to be used to contact the customer*

Name: Tamsin Heller
mail: quaylineerrands@mailvora.net
Phone: 305-482-9167

Target Market(s)

vacation home owners

Industry/Entity Type

Business

Font styles to use
Serif

Colors

Designer to choose colors to be used in the design.

Requirements
Nice to have
• Could use icons that describe the services I provide for example car, house, key, shopping cart, shopping bags, envelope, champagne glasses, phone, dog etc.

```html
<!DOCTYPE html>
<html lang="en">
<head>
<meta charset="utf-8">
<title>Harbor Concierge – Business Card</title>
<link rel="stylesheet" href="https://fonts.googleapis.com/css2?family=Cinzel:wght@500;600&family=Tinos:wght@400;700&display=swap">
<style>
  :root {
    --page: #e8e5df;
    --card: #ffffff;
    --blue: #3a56a9;
    --gold: #c9a640;
    --white: #ffffff;
  }
  * { box-sizing: border-box; margin: 0; padding: 0; }
  html, body { width: 900px; height: 1200px; overflow: hidden; }
  body { background: var(--page); position: relative; font-family: "Tinos", "Times New Roman", serif; }

  .card {
    position: absolute; left: 90px; width: 720px;
    background: var(--card); border-radius: 30px; overflow: hidden;
    box-shadow: 0 6px 18px rgba(0,0,0,.18);
  }
  .card--back { top: 135px; height: 450px; }
  .card--front { top: 630px; height: 444px; }

  .brand-title {
    position: absolute; top: 62px; left: 0; width: 100%; text-align: center;
    font-family: "Cinzel", Georgia, serif; font-weight: 600; font-size: 36px;
    letter-spacing: 1px; color: var(--blue);
  }

  .services-band {
    position: absolute; top: 156px; left: 0; width: 100%; height: 258px;
    background: var(--blue);
  }
  .service {
    position: absolute; width: 160px; margin-left: -80px; text-align: center;
    color: var(--white); font-size: 15px; line-height: 18px;
  }
  .service__icon {
    display: block; width: 60px; height: 60px; margin: 0 auto 8px;
    background: var(--white); border-radius: 50%;
  }
  .service__icon svg { display: block; width: 60px; height: 60px; }
  .service__icon svg * { fill: none; stroke: var(--blue); stroke-width: 2.4; stroke-linecap: round; stroke-linejoin: round; }
  .service__icon svg .solid { fill: var(--blue); stroke: none; }
  .row-1 { top: 30px; }
  .row-2 { top: 140px; }

  .title-banner {
    position: absolute; top: 150px; left: 0; height: 54px; width: 450px;
    background: var(--blue); color: var(--white);
    font-family: "Cinzel", Georgia, serif; font-weight: 500; font-size: 30px;
    line-height: 54px; padding-left: 62px; letter-spacing: .5px; white-space: nowrap;
    clip-path: polygon(0 0, 100% 0, 95% 100%, 0 100%);
  }
  .title-banner::before {
    content: ""; position: absolute; left: 0; top: 0; width: 42px; height: 54px; background: var(--gold);
  }

  .portrait {
    position: absolute; left: 465px; top: 15px; width: 240px; height: 339px;
    background: linear-gradient(180deg, #f2f0ee 0%, #d9cfc8 45%, #5a4a44 100%);
  }

  .gold-rule { position: absolute; left: 0; top: 354px; width: 100%; height: 6px; background: var(--gold); }
  .contact-bar {
    position: absolute; left: 0; top: 363px; width: 100%; height: 81px;
    background: var(--blue); color: var(--white); font-size: 17px;
  }
  .contact-item { position: absolute; top: 0; height: 81px; display: flex; align-items: center; white-space: nowrap; }
  .contact-name { left: 22px; font-weight: 700; }
  .contact-email { left: 212px; }
  .contact-phone { left: 538px; }
  .contact-icon {
    flex: none; width: 24px; height: 24px; margin-right: 9px;
    background: var(--white); border-radius: 50%;
  }
  .contact-icon svg { display: block; width: 24px; height: 24px; }
  .contact-icon svg * { fill: none; stroke: var(--blue); stroke-width: 1.8; stroke-linecap: round; stroke-linejoin: round; }
  .divider { position: absolute; top: 25px; width: 2px; height: 31px; background: rgba(255,255,255,.6); }
</style>
</head>
<body>

<section class="card card--back">
  <h1 class="brand-title">HARBOR CONCIERGE</h1>
  <div class="services-band">
    <div class="service row-1" style="left:111px">
      <span class="service__icon"><svg viewBox="0 0 60 60"><path d="M16 34 l4-10 h20 l4 10 v8 h-28z"/><circle class="solid" cx="22" cy="38" r="2.5"/><circle class="solid" cx="38" cy="38" r="2.5"/><path d="M18 42 v4 M42 42 v4"/></svg></span>Car</div>
    <div class="service row-1" style="left:235px">
      <span class="service__icon"><svg viewBox="0 0 60 60"><circle cx="22" cy="22" r="5"/><path d="M22 27 v20 M22 32 l16 10 v6 M38 42 h4"/></svg></span>Dog walking</div>
    <div class="service row-1" style="left:359px">
      <span class="service__icon"><svg viewBox="0 0 60 60"><path d="M20 26 h20 l-3 20 h-14z"/><path d="M22 26 q8-12 16 0"/><path d="M40 18 l4-4 M42 22 h5"/></svg></span>Cleaning</div>
    <div class="service row-1" style="left:483px">
      <span class="service__icon"><svg viewBox="0 0 60 60"><rect x="16" y="20" width="28" height="20" rx="2"/><path d="M16 21 l14 11 14-11"/></svg></span>Mail management</div>
    <div class="service row-1" style="left:607px">
      <span class="service__icon"><svg viewBox="0 0 60 60"><path d="M27 18 a3 3 0 1 1 3 4 v4 l14 12 h-28 l14-12"/><path d="M20 44 h20"/></svg></span>Stylist</div>

    <div class="service row-2" style="left:111px">
      <span class="service__icon"><svg viewBox="0 0 60 60"><path d="M14 20 h5 l4 16 h18 l3-11 h-23"/><circle class="solid" cx="25" cy="42" r="2.5"/><circle class="solid" cx="39" cy="42" r="2.5"/></svg></span>Personal shopper</div>
    <div class="service row-2" style="left:276px">
      <span class="service__icon"><svg viewBox="0 0 60 60"><circle class="solid" cx="34" cy="16" r="3.5"/><path d="M30 23 l-4 10 l6 5 l-2 10 M26 33 l-6 10 M30 23 l8 6 h5 M30 23 l-7 3 l-3 5"/></svg></span>Running errands</div>
    <div class="service row-2" style="left:442px">
      <span class="service__icon"><svg viewBox="0 0 60 60"><path d="M16 30 l14-12 14 12 M20 27 v16 h20 v-16"/><path d="M27 43 v-8 h6 v8"/></svg></span>Property management</div>
    <div class="service row-2" style="left:607px">
      <span class="service__icon"><svg viewBox="0 0 60 60"><path d="M20 18 h8 l-1 10 a3 3 0 0 1-6 0z M24 31 v12 M20 43 h8"/><path d="M33 18 h8 l-1 10 a3 3 0 0 1-6 0z M37 31 v12 M33 43 h8"/></svg></span>Event planning</div>
  </div>
</section>

<section class="card card--front">
  <div class="portrait" role="img" aria-label="Portrait photograph of the business owner"></div>
  <div class="title-banner">HARBOR CONCIERGE</div>
  <div class="gold-rule"></div>
  <div class="contact-bar">
    <span class="contact-item contact-name">Tamsin Heller</span>
    <i class="divider" style="left:195px"></i>
    <span class="contact-item contact-email"><span class="contact-icon"><svg viewBox="0 0 24 24"><rect x="6" y="8" width="12" height="9" rx="1"/><path d="M6 9 l6 4 6-4"/></svg></span>quaylineerrands@mailvora.net</span>
    <i class="divider" style="left:520px"></i>
    <span class="contact-item contact-phone"><span class="contact-icon"><svg viewBox="0 0 24 24"><path d="M8 6 h3 l1 3 -2 1.5 a8 8 0 0 0 3.5 3.5 l1.5-2 3 1 v3 a1 1 0 0 1-1 1 a11 11 0 0 1-10-10 a1 1 0 0 1 1-1z"/></svg></span>305-482-9167</span>
  </div>
</section>

</body>
</html>
```